Law Firm Needs Brochure Redesign Using New Logo

We are a personal injury law firm that does auto injuries and other personal injury cases. We want a new brochure that has our updated logo and information. Instead of gold and black, we want more navy, as matches the new logo. The Auto Liability portion should read: "(required by the state of Arizona in the amounts of $25,000 per person / $50,000 per accident, but a higher amount may be best )." The other information can remain the same. We'd like the brochure to keep the same professional tone as the previous brochure.
Our website is https://www.brandtlegalpartners.example/.

```html
<!DOCTYPE html>
<html lang="en">
<head>
<meta charset="utf-8">
<title>Brandt Legal Partners – Car Accident Brochure</title>
<link href="https://fonts.googleapis.com/css2?family=Cinzel:wght@400;700&family=Montserrat:ital,wght@0,400;0,500;1,400&family=Open+Sans:wght@400;600&display=swap" rel="stylesheet">
<style>
:root{
  --navy:#0d1a3d;
  --navy-deep:#081230;
  --royal:#1b2fa0;
  --ink:#1f2a4a;
  --paper:#ffffff;
  --panel-grey:#efefef;
  --stage:#c4c4c4;
  --photo-a:#8b8f98;
  --photo-b:#d9dade;
}
*{box-sizing:border-box;margin:0;padding:0}
html,body{width:1130px;height:1200px;overflow:hidden}
body{background:var(--stage);position:relative;font-family:'Montserrat',sans-serif;color:var(--ink)}
.sheet{position:absolute;left:160px;width:810px;height:580px;background:var(--paper);box-shadow:0 4px 14px rgba(0,0,0,.18);overflow:hidden}
.sheet--outside{top:10px}
.sheet--inside{top:610px}
.panel{position:absolute;top:0;height:100%;width:270px}
.panel--1{left:0}.panel--2{left:270px}.panel--3{left:540px}
.fold{position:absolute;top:0;bottom:0;width:1px;background:#d4d6dc}

/* outside */
.brand{position:absolute;top:48px;left:24px;display:flex;align-items:center;gap:10px}
.brand__dot{width:34px;height:34px;border-radius:50%;background:var(--navy);flex:none}
.brand__name{font-family:'Cinzel',serif;font-weight:700;font-size:19px;line-height:1.05;color:var(--navy)}
.stat{position:absolute;left:0;width:270px;text-align:center;color:var(--navy)}
.stat__over{font-family:'Cinzel',serif;font-size:14px}
.stat__num{font-family:'Cinzel',serif;font-weight:700;font-size:30px;line-height:1.05}
.stat__text{font-size:9.5px;line-height:1.35;margin-top:4px}
.stat--crashes{top:230px}
.stat--deaths{top:345px}
.promise{position:absolute;left:32px;right:22px;top:450px;text-align:center;font-size:9.5px;line-height:1.4;color:var(--navy)}
.promise::before{content:"";display:block;width:140px;height:2px;background:var(--navy);margin:0 auto 12px}
.cover-title{position:absolute;left:565px;right:26px;top:18px;text-align:center;font-family:'Cinzel',serif;font-weight:700;font-size:15.5px;line-height:1.4;color:var(--navy)}
.cover-sub{position:absolute;left:565px;right:26px;top:82px;text-align:center;font-style:italic;font-size:11.5px;line-height:1.35;color:var(--navy)}
.cover-sub__rule{display:inline-block;width:58px;height:1.5px;background:var(--navy);vertical-align:middle}
.car-photo{position:absolute;left:392px;top:200px;width:300px;height:380px;border-radius:70px 70px 0 0;background:linear-gradient(180deg,var(--royal) 0%,#121f6e 45%,#060b2a 70%,#1a2a8a 100%)}
.car-photo__split{position:absolute;left:148px;top:0;bottom:0;width:3px;background:var(--paper)}
.cover-address{position:absolute;left:772px;top:340px;width:16px;height:220px}
.cover-address p{position:absolute;left:0;top:0;width:220px;transform-origin:0 0;transform:translate(16px,0) rotate(90deg);font-size:11px;line-height:1.3;color:var(--navy);white-space:nowrap}

/* inside */
.tips{background:var(--panel-grey);padding:16px 14px 0 22px}
.tips__title{font-family:'Cinzel',serif;font-size:13px;color:var(--navy);margin-bottom:8px;padding-left:8px}
.tips__list{list-style:none}
.tips__item{position:relative;padding-left:18px;font-family:'Open Sans',sans-serif;font-size:8.6px;line-height:1.28;margin-bottom:6px;color:#2b2f3a}
.tips__item::before{content:"";position:absolute;left:-6px;top:4px;width:18px;height:3px;background:var(--navy)}
.tips__item b{font-weight:600;color:var(--navy)}
.handover-photo{position:absolute;left:270px;top:0;width:540px;height:255px;background:linear-gradient(120deg,var(--photo-a) 0%,var(--photo-b) 50%,#5d6270 100%)}
.band{position:absolute;height:30px;background:var(--navy);color:var(--paper);font-family:'Cinzel',serif;font-size:12.5px;display:flex;align-items:center;justify-content:center}
.band--coverage{left:280px;width:255px;top:255px}
.band--safety{left:540px;width:270px;top:230px}
.coverage{position:absolute;left:270px;width:270px;top:290px;bottom:0;padding:8px 12px 0 20px;background:#f6f6f7;font-family:'Open Sans',sans-serif;font-size:8.8px;line-height:1.3;color:#2b2f3a}
.coverage p{margin-bottom:6px}
.coverage b{font-weight:600;color:var(--navy)}
.safety-strip{position:absolute;left:540px;top:230px;width:28px;bottom:0;background:var(--navy)}
.safety-strip svg{position:absolute;left:6px}
.safety{position:absolute;left:574px;right:14px;top:266px;font-family:'Open Sans',sans-serif;font-size:9px;line-height:1.3;color:#2b2f3a}
.safety b{font-weight:600;color:var(--navy)}
.safety__head{font-family:'Cinzel',serif;font-weight:700;font-size:12.5px;color:var(--navy);margin:8px 0 4px}
.contact{position:absolute;left:574px;right:10px;top:420px;border-top:1.5px solid var(--navy);padding-top:6px;font-family:'Open Sans',sans-serif;font-size:9px;line-height:1.55;color:var(--ink)}
.contact__head{font-family:'Cinzel',serif;font-weight:700;font-size:12.5px;color:var(--navy);margin-bottom:4px}
</style>
</head>
<body>

<section class="sheet sheet--outside" aria-label="Brochure outside">
  <div class="panel panel--1">
    <div class="brand">
      <span class="brand__dot"></span>
      <span class="brand__name">Brandt Legal<br>Partners</span>
    </div>
    <div class="stat stat--crashes">
      <div class="stat__over">Over</div>
      <div class="stat__num">107,000</div>
      <div class="stat__text">crashes will happen in the state of<br>Arizona this year</div>
    </div>
    <div class="stat stat--deaths">
      <div class="stat__over">Over</div>
      <div class="stat__num">700</div>
      <div class="stat__text">of them will result in fatalities.</div>
    </div>
    <p class="promise">If we don't win, you don't pay attorney fees. That seems fair to us. Know what's happening with your case, get the answers to your questions and work on getting better with the confidence that you've got an excellent group of people working for you.</p>
  </div>
  <div class="fold" style="left:270px"></div>
  <div class="car-photo" role="img" aria-label="Top-down photo of a blue sports car"><span class="car-photo__split"></span></div>
  <h1 class="cover-title">Protect your family in case of a car accident</h1>
  <p class="cover-sub">A little knowledge and preparation<br><span class="cover-sub__rule"></span> go a long way <span class="cover-sub__rule"></span></p>
  <div class="cover-address"><p>4810 N. Cactus Ridge Way Suite<br>B114 Phoenix AZ 85016</p></div>
</section>

<section class="sheet sheet--inside" aria-label="Brochure inside">
  <div class="panel panel--1 tips">
    <h2 class="tips__title">Top 10 Tips to Avoid a Crash</h2>
    <ul class="tips__list">
      <li class="tips__item"><b>Anyone making a left turn must wait for all oncoming traffic to clear before proceeding.</b> Yes, even if the light has turned yellow. Wait to be sure that all traffic has stopped.</li>
      <li class="tips__item"><b>When your light turns green,</b> check to be sure that no vehicles are entering the intersection late.</li>
      <li class="tips__item"><b>Allow plenty of room between you and the car in front of you.</b> Traffic can stop in an instant, even if you can't see anything ahead.</li>
      <li class="tips__item"><b>Avoid being distracted.</b> Teenagers are especially susceptible to losing focus if there are too many friends in the car.</li>
      <li class="tips__item"><b>Keep the volume of your radio down and never wear headphones.</b> Cars are very soundproof these days, but you need to be able to hear an ambulance or police siren.</li>
      <li class="tips__item"><b>Be especially careful on the weekends and early morning hours.</b></li>
      <li class="tips__item"><b>Don't speed.</b> Speed is a factor in most crashes. Street lights are timed and the freeway has traffic. It's likely you won't get there much faster even if you do speed.</li>
      <li class="tips__item"><b>Don't drink and drive.</b> Many cab companies offer a free service to get you home safe.</li>
      <li class="tips__item"><b>Use your turn signals.</b> This gives an early warning to vehicles you may not be able to see.</li>
    </ul>
  </div>
  <div class="handover-photo" role="img" aria-label="Photo of car keys being handed over between two people"></div>
  <div class="band band--coverage">Have the Right Coverage</div>
  <div class="coverage">
    <p>Many people don't know about the different kinds of insurance available. In addition to health insurance, we suggest:</p>
    <p><b>Auto Liability</b> (required by the state of Arizona in the amounts of $25,000 per person / $50,000 per accident, but a higher amount may be best ).</p>
    <p><b>Uninsured or Underinsured Motorist Coverage.</b> This protects YOU when the other driver doesn't have insurance or not enough.</p>
    <p><b>Medical Payments Coverage.</b> Up to $5,000 in coverage will be paid out to you no matter who is at fault in an accident and does not need to be reimbursed.</p>
    <p><b>Homeowners / Renters Insurance.</b> Protects you in case of injuries on your property as well as damage to your home from covered events.</p>
  </div>
  <div class="fold" style="left:540px"></div>
  <div class="safety-strip">
    <svg style="top:80px" width="16" height="14" viewBox="0 0 16 14" aria-hidden="true"><path d="M2 1h12a1 1 0 0 1 1 1v7a1 1 0 0 1-1 1H7l-4 3v-3H2a1 1 0 0 1-1-1V2a1 1 0 0 1 1-1z" fill="#fff"/><circle cx="5" cy="5.5" r="1" fill="#0d1a3d"/><circle cx="8" cy="5.5" r="1" fill="#0d1a3d"/><circle cx="11" cy="5.5" r="1" fill="#0d1a3d"/></svg>
    <svg style="top:212px" width="14" height="14" viewBox="0 0 14 14" aria-hidden="true"><path d="M3 1l2.5 3-1.5 1.5a8 8 0 0 0 4.5 4.5L10 8.5l3 2.5-1.5 2C6 13 1 8 1 2.5z" fill="#fff"/></svg>
    <svg style="top:232px" width="14" height="14" viewBox="0 0 14 14" aria-hidden="true"><rect x="1" y="3" width="12" height="8" rx="1" fill="none" stroke="#fff" stroke-width="1.4"/><path d="M1.5 3.5L7 8l5.5-4.5" fill="none" stroke="#fff" stroke-width="1.4"/></svg>
    <svg style="top:252px" width="14" height="14" viewBox="0 0 14 14" aria-hidden="true"><circle cx="7" cy="7" r="5.5" fill="none" stroke="#fff" stroke-width="1.3"/><ellipse cx="7" cy="7" rx="2.4" ry="5.5" fill="none" stroke="#fff" stroke-width="1.1"/><path d="M1.5 7h11" stroke="#fff" stroke-width="1.1"/></svg>
    <svg style="top:274px" width="14" height="16" viewBox="0 0 14 16" aria-hidden="true"><path d="M7 1a5 5 0 0 1 5 5c0 4-5 9-5 9S2 10 2 6a5 5 0 0 1 5-5z" fill="#fff"/><circle cx="7" cy="6" r="2" fill="#0d1a3d"/></svg>
  </div>
  <div class="band band--safety">Model Safe Behavior</div>
  <div class="safety">
    <p><b>Always buckle up.</b> Always put your children in car seats/boosters that are rated for their height and weight.</p>
    <h3 class="safety__head">Never Text While Driving</h3>
    <p>Studies have shown that texting while driving is as dangerous as driving intoxicated.</p>
    <p><b>Show your children that no text is more important than your safety. It can wait.</b></p>
  </div>
  <div class="contact">
    <h3 class="contact__head">Contact Us</h3>
    <p>602.555.0147</p>
    <p>info@brandtlegalpartners.example</p>
    <p>brandtlegalpartners.example</p>
    <p>Brandt Legal Partners 4810 N. Cactus Ridge Way<br>Suite B114 Phoenix AZ 85016</p>
  </div>
</section>

</body>
</html>
```